Craft oriented film company needs a Business Card design

Hi all,
We're a 2-man band film company in New Zealand called Kestrel Pictures. We're good honest blokes, who are very passionate about the craft of film making. I've attached our current logo which has a bit of a crafty/artisan feel that we like. Feel free to use it - or throw the baby out with the bathwater and start again..... you never know, you might inspire a complete brand re-work.

In any case, the vibe we want to give out is that we are solid, dependable and no bullshit - but without compromising creative excellence and being in the now. We like the 'Brooklyn' artisan style of work.

Preferably single sided.

We need the standard stuff:
Name, job title, cellphone, email address and physical address (this can be smaller if you like - street, suburb, city & zip, country [if you want])

Check out our website to learn more about us: kestrelpictures.example

Target Market(s)

Brand marketers and advertising agency creatives looking for video production.

Industry/Entity Type

Baby

Requirements
Should not have
• Nothing flashy or too 'futuristic', we want it to feel grounded and real. A limited colour palette is preferred.
We don't want any film reels or cameras or anything obvious like that.

```html
<!DOCTYPE html>
<html lang="en">
<head>
<meta charset="utf-8">
<title>Kestrel Pictures – Business Cards</title>
<link href="https://fonts.googleapis.com/css2?family=Cinzel:wght@500&family=Lato:wght@400;700;900&display=swap" rel="stylesheet">
<style>
  :root {
    --backdrop: #e4e0da;
    --card-black: #121315;
    --card-black-soft: #1c1d20;
    --teal: #3fb4bf;
    --teal-dark: #2f98a2;
    --white: #ffffff;
    --text-light: #f2f2f2;
  }
  * { box-sizing: border-box; margin: 0; padding: 0; }
  html, body {
    width: 1200px; height: 1000px; overflow: hidden;
    background: var(--backdrop);
    font-family: "Lato", Arial, sans-serif;
  }
  .canvas {
    position: relative; width: 1200px; height: 1000px;
    display: flex; flex-direction: column; align-items: center;
    justify-content: center; gap: 36px;
  }
  .card {
    position: relative; width: 780px; height: 446px;
    border-radius: 16px; overflow: hidden;
    background: linear-gradient(160deg, var(--card-black-soft) 0%, var(--card-black) 70%);
    box-shadow: 0 8px 22px rgba(0,0,0,0.25);
  }
  .brand-mark {
    position: absolute; left: 80px; top: 92px;
    width: 180px; height: 180px; border-radius: 50%;
    background: var(--white);
    display: flex; align-items: center; justify-content: center;
    text-align: center;
  }
  .brand-name {
    font-family: "Lato", Arial, sans-serif; font-weight: 900;
    font-size: 27px; line-height: 1.05; color: var(--card-black);
    text-transform: uppercase; letter-spacing: 0.5px;
  }
  .social-links {
    position: absolute; left: 112px; top: 300px;
    display: flex; gap: 18px;
  }
  .social-dot { width: 34px; height: 34px; border-radius: 50%; background: var(--white); }
  .person-name {
    position: absolute; left: 420px; top: 40px;
    font-family: "Cinzel", Georgia, serif; font-weight: 500;
    font-size: 34px; color: var(--teal); letter-spacing: 1px;
  }
  .person-role {
    position: absolute; left: 422px; top: 94px;
    font-size: 18px; color: var(--text-light);
  }
  .contact-list {
    position: absolute; left: 440px; top: 158px;
    list-style: none; font-size: 18px; line-height: 31px; color: var(--text-light);
  }
  .contact-label { color: var(--teal); font-weight: 700; margin-right: 6px; }
  .postal-address {
    position: absolute; left: 450px; top: 272px;
    font-size: 18px; line-height: 27px; color: var(--text-light); font-style: normal;
  }
  .edge-stripe { position: absolute; left: 0; width: 100%; }
  .edge-stripe--white { top: 392px; height: 8px; background: var(--white); }
  .edge-stripe--teal {
    top: 418px; height: 28px;
    background: linear-gradient(180deg, var(--teal) 0%, var(--teal-dark) 100%);
  }
</style>
</head>
<body>
<main class="canvas">

  <article class="card">
    <div class="brand-mark"><span class="brand-name">Kestrel<br>Pictures</span></div>
    <div class="social-links" aria-label="Social media">
      <span class="social-dot"></span><span class="social-dot"></span><span class="social-dot"></span>
    </div>
    <h2 class="person-name">TOM ASHBY</h2>
    <p class="person-role">Director</p>
    <ul class="contact-list">
      <li><span class="contact-label">P:</span>+64-21-555-0142</li>
      <li><span class="contact-label">E:</span>tom@kestrelpictures.example</li>
      <li><span class="contact-label">W:</span>www.kestrelpictures.example</li>
    </ul>
    <address class="postal-address">18 Kowhai Lane, Westmere,<br>Auckland, New Zealand 1021</address>
    <div class="edge-stripe edge-stripe--white"></div>
    <div class="edge-stripe edge-stripe--teal"></div>
  </article>

  <article class="card">
    <div class="brand-mark"><span class="brand-name">Kestrel<br>Pictures</span></div>
    <div class="social-links" aria-label="Social media">
      <span class="social-dot"></span><span class="social-dot"></span><span class="social-dot"></span>
    </div>
    <h2 class="person-name">RHYS CALDER</h2>
    <p class="person-role">Producer</p>
    <ul class="contact-list">
      <li><span class="contact-label">P:</span>+64-21-555-0187</li>
      <li><span class="contact-label">E:</span>rhys@kestrelpictures.example</li>
      <li><span class="contact-label">W:</span>www.kestrelpictures.example</li>
    </ul>
    <address class="postal-address">18 Kowhai Lane, Westmere,<br>Auckland, New Zealand 1021</address>
    <div class="edge-stripe edge-stripe--white"></div>
    <div class="edge-stripe edge-stripe--teal"></div>
  </article>

</main>
</body>
</html>
```